Wine Label for new family wine label

we need a new wine label and name for our new group winemaking project. There are 10 of us in the group, plus two wine growers and two winemakers. We will be making wines on an ongoing basis but relatively small scale. The wines will be coming from the barossa valley and coonawarra. They will be high end wines - built on great dirt, some great history with the growers, and ultimately great grapes. We will be initially producing 4 wines, a shiraz, a cab, and a blend plus one high end single block shiraz based wine.

We are looking for the wine label to reflect quality, family and friendship.

```html
<!DOCTYPE html>
<html lang="en">
<head>
<meta charset="utf-8">
<title>Kinfold Cabernet 2013 — Wine Label</title>
<link href="https://fonts.googleapis.com/css2?family=Questrial&family=Cormorant+Garamond:wght@500&display=swap" rel="stylesheet">
<style>
  :root {
    --backdrop: #222222;
    --label: #000000;
    --label-edge: #2c2c2c;
    --brand-ink: #cfcfcf;
    --detail-ink: #e6e6e6;
    --ornament-glow: #262626;
    --ornament-fade: rgba(0, 0, 0, 0);
  }
  html, body {
    margin: 0;
    padding: 0;
    width: 1200px;
    height: 900px;
    overflow: hidden;
    background: var(--backdrop);
  }
  .canvas {
    position: relative;
    width: 1200px;
    height: 900px;
    background: var(--backdrop);
  }
  .wine-label {
    position: absolute;
    left: 351px;
    top: 132px;
    width: 498px;
    height: 636px;
    background: var(--label);
    box-shadow: 0 0 0 1px var(--label-edge);
  }
  .label-ornament {
    position: absolute;
    left: 149px;
    top: 130px;
    width: 248px;
    height: 295px;
    background: radial-gradient(ellipse at 45% 50%, var(--ornament-glow) 0%, var(--ornament-fade) 70%);
  }
  .brand-name {
    position: absolute;
    left: 0;
    right: 0;
    top: 188px;
    margin: 0;
    text-align: center;
    font-family: "Questrial", "Century Gothic", sans-serif;
    font-weight: 400;
    font-size: 74px;
    line-height: 1;
    letter-spacing: 0.01em;
    color: var(--brand-ink);
  }
  .varietal {
    position: absolute;
    left: 0;
    right: 0;
    top: 466px;
    margin: 0;
    text-align: center;
    font-family: "Cormorant Garamond", "Times New Roman", serif;
    font-weight: 500;
    font-size: 30px;
    font-variant: small-caps;
    letter-spacing: 0.55em;
    padding-left: 0.55em;
    line-height: 1;
    color: var(--detail-ink);
  }
  .vintage {
    position: absolute;
    left: 0;
    right: 0;
    top: 513px;
    margin: 0;
    text-align: center;
    font-family: "Cormorant Garamond", "Times New Roman", serif;
    font-weight: 500;
    font-size: 32px;
    font-variant-numeric: lining-nums;
    letter-spacing: 0.4em;
    padding-left: 0.4em;
    line-height: 1;
    color: var(--detail-ink);
  }
</style>
</head>
<body>
  <main class="canvas">
    <section class="wine-label">
      <div class="label-ornament" role="img" aria-label="Faint decorative numeral with a curling vine flourish behind the brand name"></div>
      <h1 class="brand-name">kinfold</h1>
      <p class="varietal">Cabernet</p>
      <p class="vintage">2013</p>
    </section>
  </main>
</body>
</html>
```